Business Card

We need some ideas for corporate business cards. I'm interested in a double sided card, with one side featuring our corporate logo, the other side with employee information.

Corporate colors, logo etc. available at www.brivalo.com

Industry/Entity Type

Business

Requirements
Must have
• The "Brivalo" logo with stylized "O"

Nice to have
• Preferred font is calibri

```html
<!DOCTYPE html>
<html lang="en">
<head>
<meta charset="utf-8">
<title>Brivalo Business Card</title>
<link rel="stylesheet" href="https://fonts.googleapis.com/css2?family=Carlito:wght@400;700&display=swap">
<style>
  :root {
    --bg: #d4d5d7;
    --card: #fbfbfb;
    --ink: #0a0a0a;
    --orange: #e8871d;
    --contact: #a9a9a9;
    --white: #ffffff;
  }
  * { margin: 0; padding: 0; box-sizing: border-box; }
  html, body { width: 1200px; height: 1000px; overflow: hidden; }
  body {
    background: var(--bg);
    font-family: "Carlito", Calibri, sans-serif;
    display: flex;
    flex-direction: column;
    align-items: center;
    justify-content: center;
    gap: 56px;
  }
  .card {
    position: relative;
    width: 640px;
    height: 366px;
    background: var(--card);
    box-shadow: 0 6px 18px rgba(0,0,0,0.12);
    overflow: hidden;
  }

  /* Logo side */
  .brand-band {
    position: absolute;
    left: 26px;
    top: 190px;
    width: 380px;
    height: 72px;
    background: var(--ink);
    display: flex;
    align-items: center;
    padding-left: 34px;
  }
  .brand-name {
    color: var(--white);
    font-size: 52px;
    font-weight: 400;
    letter-spacing: 6px;
    text-transform: uppercase;
    line-height: 1;
  }
  .web-block {
    position: absolute;
    right: 0;
    top: 178px;
    width: 214px;
    height: 72px;
    background: var(--orange);
    display: flex;
    align-items: center;
    padding-left: 22px;
  }
  .web-address {
    color: var(--white);
    font-size: 19px;
    font-weight: 700;
  }

  /* Employee side */
  .name-band {
    position: absolute;
    left: 0;
    top: 140px;
    width: 284px;
    height: 66px;
    background: var(--ink);
    padding: 10px 0 0 36px;
    color: var(--white);
  }
  .person-name {
    font-size: 26px;
    font-weight: 700;
    line-height: 1.05;
  }
  .designation {
    font-size: 15px;
    font-weight: 400;
  }
  .contact-list {
    position: absolute;
    left: 304px;
    top: 138px;
    width: 190px;
    list-style: none;
    color: var(--contact);
    font-size: 15px;
    line-height: 22px;
    white-space: nowrap;
  }
  .contact-list .label {
    display: inline-block;
    width: 24px;
  }
  .accent-block {
    position: absolute;
    right: 0;
    top: 140px;
    width: 134px;
    height: 66px;
    background: var(--orange);
  }
</style>
</head>
<body>
  <section class="card card-logo-side" aria-label="Business card, logo side">
    <div class="brand-band"><span class="brand-name">Brivalo</span></div>
    <div class="web-block"><span class="web-address">www.brivalo.com</span></div>
  </section>

  <section class="card card-employee-side" aria-label="Business card, employee side">
    <div class="name-band">
      <p class="person-name">Person Name</p>
      <p class="designation">designation</p>
    </div>
    <ul class="contact-list">
      <li><span class="label">P :</span> 555 0142 3360</li>
      <li><span class="label">F :</span> 555 0142 3360</li>
      <li><span class="label">E :</span> info@brivalo.com</li>
    </ul>
    <div class="accent-block"></div>
  </section>
</body>
</html>
```